Business card design for new eCommerce site focusing on integrity and strong businsess tactics

We need a business card that will stand out and be memorable. Something with color that matches our company logo colors. Think high end version of Dealvine. There are 2 logos provided. The parent company is called Bright Harbor Ventures and we are presenting a new and very exciting eCommerce site called KeenTraders.example.

Target Market(s)

Our target markets are in the Activities, Food and Beverage, Health and Beauty

Industry/Entity Type

Marketing

Contact Information for Business Card

We have 4 members that need cards...I will provide all info to the winner of the design contest
Business Address is
48730 West 61st Avenue, Suite C204
Phoenix AZ 85917

Font styles to use
Serif
Sans Serif

Colors

Designer to choose colors to be used in the design.

Requirements
Must have
• The card must be memorable...should be unique in design but must exude integrity and be playful .
• I have provided several colors or our parent company...please feel free to use which ever
Nice to have
• I will leave this up to you. Feel free to use other images of your choosing that wraps around our client.....Activities, Dining, Health, Beauty
Should not have
• just dont be boring

```html
<!DOCTYPE html>
<html lang="en">
<head>
<meta charset="utf-8">
<title>Bright Harbor Ventures – Business Card</title>
<link rel="stylesheet" href="https://fonts.googleapis.com/css2?family=Roboto:wght@300;400;500;700&display=swap">
<style>
  :root {
    --backdrop: #a9a9a9;
    --lime: #8db63a;
    --teal: #1f7b7b;
    --teal-mid: #3a9690;
    --teal-text: #2e8f89;
    --charcoal: #3b3d3f;
    --paper: #f4f4f2;
    --white: #ffffff;
    --ink: #333333;
  }
  * { box-sizing: border-box; margin: 0; padding: 0; }
  html, body { width: 1200px; height: 576px; overflow: hidden; }
  body {
    background: var(--backdrop);
    font-family: "Roboto", Arial, sans-serif;
    position: relative;
  }
  .card {
    position: absolute;
    border-radius: 14px;
    overflow: hidden;
  }

  /* Front */
  .card-front {
    left: 82px; top: 139px; width: 484px; height: 293px;
    background: linear-gradient(180deg, var(--lime) 0%, #79ad45 30%, #2f8a76 62%, var(--teal) 100%);
  }
  .front-mark {
    position: absolute; left: 182px; top: 55px;
    width: 120px; height: 120px; border-radius: 50%;
    background: var(--white);
    box-shadow: 0 0 0 2px var(--lime), 0 0 0 3px rgba(255,255,255,.8);
  }
  .front-name {
    position: absolute; left: 0; right: 0; top: 186px;
    text-align: center; color: var(--white);
    font-weight: 700; font-size: 29px; line-height: 1;
  }
  .front-sub {
    position: absolute; left: 0; right: 0; top: 219px;
    text-align: center; color: var(--white);
    font-weight: 300; font-size: 13px; letter-spacing: 4px; line-height: 1;
  }

  /* Back */
  .card-back {
    left: 602px; top: 138px; width: 480px; height: 292px;
    background: var(--paper);
  }
  .back-mark {
    position: absolute; left: 64px; top: 20px;
    width: 136px; height: 136px; border-radius: 50%;
    background: var(--teal-mid);
    box-shadow: 0 0 0 3px var(--paper), 0 0 0 5px var(--teal-mid);
  }
  .back-name {
    position: absolute; left: 24px; top: 167px;
    color: var(--teal-text); font-weight: 700; font-size: 30px; line-height: 1;
  }
  .back-sub {
    position: absolute; left: 24px; top: 200px; width: 210px;
    text-align: center; color: var(--teal-text);
    font-weight: 300; font-size: 13px; letter-spacing: 4px; line-height: 1;
  }
  .wave { position: absolute; left: 0; top: 0; }
  .person {
    position: absolute; right: 17px; top: 32px; text-align: right;
  }
  .person-name { color: var(--teal-text); font-weight: 700; font-size: 21px; line-height: 1.1; }
  .person-role { color: var(--ink); font-size: 12px; margin-top: 5px; }
  .partner {
    position: absolute; right: 17px; top: 108px;
    display: flex; align-items: center; gap: 6px;
    color: var(--teal-text); font-weight: 500; font-size: 15px;
  }
  .partner-dot { width: 12px; height: 12px; border-radius: 50%; background: var(--lime); }
  .contact {
    position: absolute; right: 17px; top: 206px; text-align: right;
    color: var(--white); font-size: 12.5px; line-height: 18px;
  }
  .contact-line { display: flex; justify-content: flex-end; align-items: center; gap: 6px; }
  .contact-line svg { width: 11px; height: 11px; }
  .contact-address { margin-top: 2px; }
</style>
</head>
<body>

  <section class="card card-front" aria-label="Card front">
    <div class="front-mark"></div>
    <div class="front-name">Bright Harbor</div>
    <div class="front-sub">ventures</div>
  </section>

  <section class="card card-back" aria-label="Card back">
    <svg class="wave" width="480" height="292" viewBox="0 0 480 292" aria-hidden="true">
      <path d="M0 250 C120 272 250 252 330 202 C390 164 440 152 480 154 L480 292 L0 292 Z" fill="var(--teal-mid)"/>
      <path d="M0 212 C70 236 180 246 262 232 C200 250 80 250 0 236 Z" fill="var(--lime)"/>
      <path d="M40 230 C180 252 300 232 352 190 C400 152 440 142 480 138 L480 146 C440 150 404 160 356 198 C300 242 170 252 40 230 Z" fill="var(--charcoal)"/>
    </svg>

    <div class="back-mark"></div>
    <div class="back-name">Bright Harbor</div>
    <div class="back-sub">ventures</div>

    <div class="person">
      <div class="person-name">Employee Name</div>
      <div class="person-role">Managing Director</div>
    </div>

    <div class="partner"><span class="partner-dot"></span>Wellvue.example</div>

    <div class="contact">
      <div class="contact-line">1800-555-0142
        <svg viewBox="0 0 12 12" aria-hidden="true"><path d="M2 1h3l1 3-1.5 1a7 7 0 0 0 2.5 2.5L8 6l3 1v3a1 1 0 0 1-1 1A9 9 0 0 1 1 2a1 1 0 0 1 1-1z" fill="#fff"/></svg>
      </div>
      <div class="contact-line">www.keentraders.example
        <svg viewBox="0 0 12 12" aria-hidden="true"><rect x="1" y="2.5" width="10" height="7" fill="#fff"/><path d="M1 2.5l5 4 5-4" fill="none" stroke="var(--teal-mid)" stroke-width="1"/></svg>
      </div>
      <div class="contact-line">name@keentraders.example
        <svg viewBox="0 0 12 12" aria-hidden="true"><circle cx="6" cy="6" r="5" fill="none" stroke="#fff"/><ellipse cx="6" cy="6" rx="2" ry="5" fill="none" stroke="#fff"/><path d="M1 6h10" stroke="#fff"/></svg>
      </div>
      <div class="contact-address">48730 West 61st Avenue, Suite C204, Phoenix AZ 85917</div>
    </div>
  </section>

</body>
</html>
```